Brennick Holdings Business Cards

These are professional business cards that are for my family office.
Put fake emails and phone numbers as of now until I finalize those components. This family office controls my families investments, assets, and future. The cards should be professional.
..
.
.
.
I just uploaded another variation of a logo I would like to see as a business card to I am inbeteen which logo to use

Target Market(s)

business

Industry/Entity Type

business

Contact Information for Business Card

Professional, wealth related, finance related.

Requirements
Must have
• Logo

```html
<!DOCTYPE html>
<html lang="en">
<head>
<meta charset="utf-8">
<title>Brennick Holdings – Business Cards</title>
<link rel="stylesheet" href="https://fonts.googleapis.com/css2?family=Cinzel:wght@500;600&family=Tinos:wght@400;700&display=swap">
<style>
  :root {
    --bg: #e4e4e4;
    --card: #050505;
    --white: #ffffff;
    --grey: #a9a9a9;
    --shadow: rgba(0, 0, 0, 0.28);
  }
  * { margin: 0; padding: 0; box-sizing: border-box; }
  html, body { width: 1200px; height: 813px; overflow: hidden; }
  body {
    background: radial-gradient(circle at 45% 40%, #f3f3f3 0%, var(--bg) 70%);
    position: relative;
    font-family: "Tinos", "Times New Roman", serif;
    color: var(--white);
  }
  .card {
    position: absolute;
    width: 540px;
    height: 308px;
    background: var(--card);
    box-shadow: 0 12px 28px var(--shadow);
    overflow: hidden;
  }
  .card--front { left: 40px; top: 180px; }
  .card--back { left: 620px; top: 325px; }

  /* front */
  .front-mark {
    position: absolute;
    left: 50%; top: 44px;
    width: 128px; height: 128px;
    margin-left: -64px;
    border: 3px solid var(--white);
    border-radius: 50%;
  }
  .front-name {
    position: absolute;
    left: 0; right: 0; top: 198px;
    text-align: center;
    font-family: "Cinzel", Georgia, serif;
    font-weight: 500;
    font-size: 34px;
    letter-spacing: 1px;
    color: var(--white);
  }

  /* back */
  .back-name {
    position: absolute;
    left: 28px; top: 46px;
    font-family: "Cinzel", Georgia, serif;
    font-weight: 500;
    font-size: 25px;
    letter-spacing: 0.5px;
  }
  .person {
    position: absolute;
    left: 28px; top: 112px;
  }
  .person__name { font-weight: 700; font-size: 20px; line-height: 1.2; }
  .person__title { font-size: 15px; line-height: 1.4; }
  .person__rule {
    width: 18px; height: 4px; background: var(--white);
    margin-top: 10px;
  }
  .contact {
    position: absolute;
    left: 28px; top: 190px;
    list-style: none;
    font-size: 15px;
    line-height: 24px;
  }
  .contact li { display: flex; align-items: center; gap: 7px; }
  .contact svg { width: 14px; height: 14px; fill: var(--white); }
  .band-white {
    position: absolute;
    left: 0; right: 0; top: 244px; height: 24px;
    background: var(--white);
  }
  .band-bottom {
    position: absolute;
    left: 0; width: 370px; bottom: 10px; height: 16px;
    background: var(--white);
  }
  .band-grey {
    position: absolute;
    left: 440px; right: 0; top: 160px; height: 30px;
    background: var(--grey);
  }
  .back-mark {
    position: absolute;
    left: 410px; top: 150px;
    width: 50px; height: 50px;
    border-radius: 50%;
    background: var(--card);
    border: 2px solid var(--white);
  }
</style>
</head>
<body>
  <section class="card card--front" aria-label="Business card front">
    <div class="front-mark"></div>
    <p class="front-name">Brennick Holdings</p>
  </section>

  <section class="card card--back" aria-label="Business card back">
    <p class="back-name">Brennick Holdings</p>
    <div class="person">
      <p class="person__name">Daniel Hale</p>
      <p class="person__title">Founder</p>
      <div class="person__rule"></div>
    </div>
    <ul class="contact">
      <li>
        <svg viewBox="0 0 24 24" aria-hidden="true"><path d="M6.6 10.8a15.1 15.1 0 0 0 6.6 6.6l2.2-2.2a1 1 0 0 1 1-.25 11.4 11.4 0 0 0 3.6.57 1 1 0 0 1 1 1V20a1 1 0 0 1-1 1A17 17 0 0 1 3 4a1 1 0 0 1 1-1h3.5a1 1 0 0 1 1 1c0 1.25.2 2.45.57 3.57a1 1 0 0 1-.25 1z"/></svg>
        555-210-4387
      </li>
      <li>
        <svg viewBox="0 0 24 24" aria-hidden="true"><path d="M2 5h20v14H2zm2 2v.5l8 5 8-5V7zm0 2.8V17h16V9.8l-8 5z"/></svg>
        office@brennickmail.com
      </li>
    </ul>
    <div class="band-grey"></div>
    <div class="back-mark"></div>
    <div class="band-white"></div>
    <div class="band-bottom"></div>
  </section>
</body>
</html>
```